New more attractive design for an old tired look that is high tech but inviting

Need a more modern eye catching design. We are and I/T and MSP and we need a new look. Need a call to action on each page. Needs to be in WordPress. Existing site is brivanoqe.com. Needs to work on phones and tablets. The default home page should present us as an MSP/MSSP and direct the viewer to our services we offer.
Updates

Current deadline assigned at project inception has passed before project started

Need extra days to review

Target Market(s)

Our target market is other businesses. We do not target residential customers.

Industry/Entity Type

Business to Business oriented

Coding

Coded - Design and coding required

Number of Pages Required

5+ page

Font styles to use
Sans Serif

Requirements
Must have
• Must have a current relevant design with a call to action on each page.
Nice to have
• Dark background high tech look with people to make it attractive

```html
<!DOCTYPE html>
<html lang="en">
<head>
<meta charset="utf-8">
<title>Brivano Systems – Data Center Services</title>
<link href="https://fonts.googleapis.com/css2?family=Poppins:wght@400;500;600;700&display=swap" rel="stylesheet">
<style>
:root{
  --red:#c0262d;
  --dark:#2f434e;
  --header:#262626;
  --ink:#1c1c1c;
  --muted:#555;
  --blush:#fbeeee;
  --form:#f2f4f5;
  --white:#fff;
}
*{box-sizing:border-box;margin:0;padding:0}
html,body{width:1200px;height:2808px;overflow:hidden}
body{font-family:"Poppins",sans-serif;color:var(--ink);background:var(--white);position:relative}
.abs{position:absolute}
.brand{color:var(--white);font-weight:600;font-size:26px;line-height:1;display:flex;align-items:center;gap:8px;white-space:nowrap}
.brand i{width:10px;height:10px;background:var(--red);display:block}
.site-header{left:0;top:0;width:1200px;height:82px;background:var(--header)}
.nav a{position:absolute;top:36px;color:#eee;font-size:15px;text-decoration:none}
.nav a.active::after{content:"";position:absolute;left:0;right:0;bottom:-33px;height:3px;background:var(--red)}
.btn{display:flex;align-items:center;gap:14px;background:var(--red);color:var(--white);font-weight:600;font-size:15px;letter-spacing:.5px;padding:0 14px}
.btn::after{content:"";position:absolute;right:-12px;top:0;width:6px;height:100%;background:var(--red)}
.hero{left:0;top:82px;width:1200px;height:631px;background:linear-gradient(90deg,#2a3034 0%,#3a3f42 40%,#6b6762 65%,#3d3b38 100%)}
.hero h1{position:absolute;left:57px;top:150px;color:var(--white);font-size:63px;line-height:62px;font-weight:600}
.hero p{position:absolute;left:59px;top:295px;width:470px;color:#eee;font-size:14px;line-height:23px;border-left:2px solid #fff;padding-left:10px}
.feature{top:713px;width:284px;height:187px;text-align:center;border-top:3px solid var(--dark);padding:51px 40px 0}
.feature.hl{background:var(--blush);border-top-color:var(--red)}
.feature h3{font-size:18px;font-weight:600;margin-bottom:6px}
.feature p{font-size:12.5px;line-height:19.5px;color:var(--muted)}
.ficon{top:674px;width:70px;height:70px;background:var(--dark);display:flex;align-items:center;justify-content:center;border:1px solid #fff}
.ficon.hl{background:var(--red)}
.dashes{height:7px;background:repeating-linear-gradient(90deg,var(--red) 0 5px,transparent 5px 9px)}
.about{left:0;top:1014px;width:1140px;height:412px;background:var(--dark);color:var(--white)}
.about .kicker{position:absolute;left:61px;top:78px;font-size:18px}
.about h2{position:absolute;left:61px;top:106px;font-size:29px;font-weight:600}
.about .text{position:absolute;left:61px;top:165px;width:540px;font-size:13px;line-height:19.5px;color:#e5e9eb}
.about .text p+p{margin-top:10px}
.section-title{left:0;width:1200px;text-align:center;color:var(--dark);font-size:30px;font-weight:600}
.svc{top:1581px;width:204px;height:278px;background:var(--blush);text-align:center}
.svc .ph{height:195px}
.svc .sicon{position:absolute;left:75px;top:160px;width:54px;height:54px;background:var(--red);border:1px solid #fff;display:flex;align-items:center;justify-content:center}
.svc h4{position:absolute;left:0;right:0;top:222px;font-size:15.5px;font-weight:600;line-height:21px;color:var(--dark)}
.info h5{font-size:15.5px;font-weight:600;display:flex;align-items:center;gap:14px}
.info p{font-size:13px;color:var(--muted);line-height:21px;margin-top:6px}
.footer{left:0;top:2402px;width:1200px;height:406px;background:var(--dark)}
.form{left:195px;top:2123px;width:810px;height:412px;background:var(--form)}
.form h2{position:absolute;left:0;right:0;top:42px;text-align:center;font-size:29px;font-weight:600;color:var(--dark)}
.field{position:absolute;border-bottom:1px solid #c9cfd2;font-size:12.5px;font-weight:500;color:#444}
.field.first{border-bottom:2px solid #8a959b}
.ficn{width:43px;height:43px;background:var(--red);display:flex;align-items:center;justify-content:center}
.foot-txt{color:var(--white);font-size:13px}
</style>
</head>
<body>

<header class="abs site-header">
  <nav class="nav">
    <a href="#" class="active" style="left:61px">Home</a>
    <a href="#" style="left:138px">About Us</a>
    <a href="#" style="left:236px">Services</a>
    <a href="#" style="left:328px">Contact Us</a>
  </nav>
  <div class="abs brand" style="left:508px;top:28px"><i></i>Brivano Systems</div>
  <a class="abs btn" style="left:953px;top:22px;height:40px;text-decoration:none">
    <svg width="22" height="22" viewBox="0 0 24 24"><path fill="#fff" d="M6.6 10.8a15 15 0 0 0 6.6 6.6l2.2-2.2c.3-.3.7-.4 1-.2 1.1.4 2.3.6 3.6.6.6 0 1 .4 1 1V20c0 .6-.4 1-1 1A17 17 0 0 1 3 4c0-.6.4-1 1-1h3.5c.6 0 1 .4 1 1 0 1.3.2 2.5.6 3.6.1.3 0 .7-.2 1z"/></svg>
    555-014-2736
  </a>
</header>

<section class="abs hero" role="img" aria-label="Photo of a smiling businesswoman holding a tablet in an office">
  <h1>Data Center<br>Services</h1>
  <p>We offer colocation, virtualization, storage as a service and disaster recovery out of our own enterprise-grade data center.</p>
  <a class="abs btn" style="left:60px;top:363px;height:40px;text-decoration:none">
    <svg width="22" height="22" viewBox="0 0 24 24"><path fill="#fff" d="M6.6 10.8a15 15 0 0 0 6.6 6.6l2.2-2.2c.3-.3.7-.4 1-.2 1.1.4 2.3.6 3.6.6.6 0 1 .4 1 1V20c0 .6-.4 1-1 1A17 17 0 0 1 3 4c0-.6.4-1 1-1h3.5c.6 0 1 .4 1 1 0 1.3.2 2.5.6 3.6.1.3 0 .7-.2 1z"/></svg>
    555-014-2736
  </a>
</section>

<div class="abs feature" style="left:141px"><h3>A True Partner</h3><p>One size data center architecture does not fit all. We take the time to understand your specific requirements.</p></div>
<div class="abs feature hl" style="left:458px"><h3>High Security</h3><p>Our data center is a Tier III, standalone structure designed to withstand wind speeds up to 206mph.</p></div>
<div class="abs feature" style="left:773px"><h3>Availability</h3><p>The facility is powered by two separate utility feeds and a Korvath diesel generator.</p></div>

<div class="abs ficon" style="left:249px"><svg width="40" height="40" viewBox="0 0 40 40" fill="none" stroke="#fff" stroke-width="2"><path d="M4 14l8-6 8 4 8-4 8 6"/><path d="M8 18l8 8 4-2 4 4 4-2 6-8"/><path d="M14 22l4 4M18 20l4 4"/></svg></div>
<div class="abs ficon hl" style="left:565px"><svg width="40" height="40" viewBox="0 0 40 40" fill="none" stroke="#fff" stroke-width="2"><path d="M20 4l13 5v10c0 8-6 14-13 17C13 33 7 27 7 19V9z"/><circle cx="20" cy="19" r="7"/><path d="M16 19l3 3 5-5"/></svg></div>
<div class="abs ficon" style="left:881px"><svg width="40" height="40" viewBox="0 0 40 40" fill="none" stroke="#fff" stroke-width="2"><ellipse cx="24" cy="8" rx="7" ry="3"/><path d="M17 8v8c0 2 3 3 7 3s7-1 7-3V8M17 12c0 2 3 3 7 3s7-1 7-3"/><path d="M4 28l7-4h8l5 3-5 2h-6M4 34l10 0 16-8"/></svg></div>

<div class="abs" style="left:916px;top:976px;width:284px;height:359px;background:var(--red)"></div>
<section class="abs about">
  <div class="kicker">About</div>
  <h2>Brivano Systems</h2>
  <div class="abs dashes" style="left:61px;top:143px;width:80px"></div>
  <div class="abs" style="left:141px;top:146px;width:60px;height:1px;background:var(--red)"></div>
  <div class="text">
    <p>Like most great businesses Brivano Systems began in a garage during the summer of 1995 in Larkfield, SC. It was a part time venture by Marcus Delvane and his business partner Owen Talbrook. They had discovered an opportunity in technology sales and service after a combined 30 years at Harlow Power in information technology.</p>
    <p>Today, the company has grown significantly and continues to do so. Brivano Systems provides services including multi-dwelling unit managed networks, data center services, low voltage wiring and local office IT support. Industries served include: retail, manufacturing, MDUs, hospitality, software development, medical, construction and more.</p>
  </div>
  <div class="abs" role="img" aria-label="Photo of two colleagues looking at a computer monitor" style="left:670px;top:26px;width:445px;height:360px;background:linear-gradient(135deg,#9fb3c4,#5d7284 60%,#3d4a56)"></div>
</section>

<h2 class="abs section-title" style="top:1494px">Our Services</h2>
<div class="abs dashes" style="left:510px;top:1535px;width:80px"></div>
<div class="abs" style="left:590px;top:1532px;width:48px;height:1px;background:var(--red)"></div>

<div class="abs svc" style="left:60px"><div class="ph" role="img" aria-label="Photo of hands typing with cybersecurity graphics" style="background:linear-gradient(160deg,#4d6c8c,#1f3346)"></div><div class="sicon"><svg width="30" height="30" viewBox="0 0 30 30" fill="none" stroke="#fff" stroke-width="1.6"><rect x="9" y="13" width="12" height="10"/><path d="M11 13v-3a4 4 0 0 1 8 0v3"/><circle cx="15" cy="18" r="1.5"/></svg></div><h4>Managed<br>Cybersecurity</h4></div>
<div class="abs svc" style="left:279px"><div class="ph" role="img" aria-label="Photo of a hand holding digital transformation icons" style="background:linear-gradient(160deg,#3a4048,#15191e)"></div><div class="sicon"><svg width="30" height="30" viewBox="0 0 30 30" fill="none" stroke="#fff" stroke-width="1.6"><circle cx="15" cy="10" r="5"/><path d="M5 26c2-6 6-8 10-8s8 2 10 8"/></svg></div><h4>Managed Networks<br>for MDUs</h4></div>
<div class="abs svc" style="left:498px"><div class="ph" role="img" aria-label="Photo of two technicians working in a server room" style="background:linear-gradient(160deg,#3b5a70,#12202c)"></div><div class="sicon"><svg width="30" height="30" viewBox="0 0 30 30" fill="none" stroke="#fff" stroke-width="1.6"><rect x="5" y="6" width="20" height="5"/><rect x="5" y="13" width="20" height="5"/><rect x="5" y="20" width="20" height="5"/></svg></div><h4>Data Center<br>Services</h4></div>
<div class="abs svc" style="left:717px"><div class="ph" role="img" aria-label="Photo of a wiring panel with network cables" style="background:linear-gradient(160deg,#c9ccc9,#8f9590)"></div><div class="sicon"><svg width="30" height="30" viewBox="0 0 30 30" fill="none" stroke="#fff" stroke-width="1.6"><path d="M16 4l-7 12h6l-2 10 8-13h-6z"/></svg></div><h4>Low Voltage<br>Wiring</h4></div>
<div class="abs svc" style="left:936px"><div class="ph" role="img" aria-label="Photo of a technician repairing a computer at a desk" style="background:linear-gradient(160deg,#9aa4ad,#4a545d)"></div><div class="sicon"><svg width="30" height="30" viewBox="0 0 30 30" fill="none" stroke="#fff" stroke-width="1.6"><rect x="4" y="6" width="22" height="15"/><path d="M11 25h8M15 21v4"/><circle cx="15" cy="13" r="3"/></svg></div><h4>Office IT<br>Support</h4></div>

<h2 class="abs section-title" style="top:1928px">Contact Us</h2>
<div class="abs dashes" style="left:521px;top:1968px;width:80px"></div>
<div class="abs" style="left:601px;top:1965px;width:36px;height:1px;background:var(--red)"></div>

<div class="abs info" style="left:209px;top:2017px"><h5><svg width="20" height="20" viewBox="0 0 24 24"><path fill="#c0262d" d="M6.6 10.8a15 15 0 0 0 6.6 6.6l2.2-2.2c.3-.3.7-.4 1-.2 1.1.4 2.3.6 3.6.6.6 0 1 .4 1 1V20c0 .6-.4 1-1 1A17 17 0 0 1 3 4c0-.6.4-1 1-1h3.5c.6 0 1 .4 1 1 0 1.3.2 2.5.6 3.6.1.3 0 .7-.2 1z"/></svg>Call Us</h5><p>555-014-2736.</p></div>
<div class="abs" style="left:456px;top:2020px;width:1px;height:62px;background:#ccc"></div>
<div class="abs info" style="left:484px;top:2017px"><h5><svg width="20" height="16" viewBox="0 0 20 16"><rect width="20" height="16" fill="#c0262d"/><path d="M1 1l9 7 9-7" stroke="#fff" stroke-width="1.6" fill="none"/></svg>Email</h5><p>support@brivanoqe.com</p></div>
<div class="abs" style="left:730px;top:2020px;width:1px;height:62px;background:#ccc"></div>
<div class="abs info" style="left:756px;top:2022px"><h5><svg width="16" height="20" viewBox="0 0 16 20"><path fill="#c0262d" d="M8 0a8 8 0 0 1 8 8c0 6-8 12-8 12S0 14 0 8a8 8 0 0 1 8-8z"/><circle cx="8" cy="8" r="3" fill="#fff"/></svg>Location</h5><p>Brivano Systems 48 Ridgeline Way<br>Larkfield, SC 29000</p></div>

<footer class="abs footer">
  <div class="abs brand" style="left:60px;top:192px"><i></i>Brivano Systems</div>
  <div class="abs foot-txt" style="left:61px;top:290px">Home | Services | About | Contact</div>
  <div class="abs foot-txt" style="left:61px;top:317px">2025 © Brivano Systems of SC, Inc.</div>
  <div class="abs" style="left:600px;top:180px;width:1px;height:185px;background:#5a6d77"></div>
  <div class="abs ficn" style="left:639px;top:182px"><svg width="20" height="20" viewBox="0 0 24 24"><path fill="#fff" d="M6.6 10.8a15 15 0 0 0 6.6 6.6l2.2-2.2c.3-.3.7-.4 1-.2 1.1.4 2.3.6 3.6.6.6 0 1 .4 1 1V20c0 .6-.4 1-1 1A17 17 0 0 1 3 4c0-.6.4-1 1-1h3.5c.6 0 1 .4 1 1 0 1.3.2 2.5.6 3.6.1.3 0 .7-.2 1z"/></svg></div>
  <div class="abs foot-txt" style="left:706px;top:183px;font-size:15.5px;font-weight:600">Call Us</div>
  <div class="abs foot-txt" style="left:707px;top:210px">555-014-2736.</div>
  <div class="abs ficn" style="left:639px;top:280px"><svg width="16" height="20" viewBox="0 0 16 20"><path fill="#fff" d="M8 0a8 8 0 0 1 8 8c0 6-8 12-8 12S0 14 0 8a8 8 0 0 1 8-8z"/><circle cx="8" cy="8" r="3" fill="#c0262d"/></svg></div>
  <div class="abs foot-txt" style="left:706px;top:284px;font-size:15.5px;font-weight:600">Location</div>
  <div class="abs foot-txt" style="left:707px;top:311px;line-height:21px">Brivano Systems 48 Ridgeline Way<br>Larkfield, SC 29000</div>
</footer>

<section class="abs form">
  <h2>Get In Touch</h2>
  <div class="field first" style="left:50px;top:112px;width:336px;height:48px">First Name</div>
  <div class="field" style="left:425px;top:112px;width:336px;height:48px">Last Name</div>
  <div class="field" style="left:50px;top:172px;width:336px;height:48px">Email</div>
  <div class="field" style="left:425px;top:172px;width:336px;height:48px">Phone Number</div>
  <div class="field" style="left:50px;top:232px;width:711px;height:78px">Message</div>
  <div class="abs btn" style="left:319px;top:325px;height:41px;padding:0 24px;font-size:15.5px">Send Message</div>
</section>

</body>
</html>
```